Aunt Rolina's Bakery

I am about to create a luxury boutique that specializes in cake baking and cupcake
and ready for parties and special events and order delivery
the logo has already made

Industry/Entity Type

Boutique

Contact Information for Business Card

Email:auntrolinasbakery@maplecrumbmail.com
Instagram: aunt_rolina_bakery
Twitter: xxxxxxx
WhatsApp: xxxxxxx

Requirements
Must have
• luxury design

```html
<!DOCTYPE html>
<html lang="en">
<head>
<meta charset="UTF-8">
<title>Aunt Rolina's Bakery – Business Card</title>
<link href="https://fonts.googleapis.com/css2?family=Cinzel:wght@400;500&family=Roboto:wght@400&display=swap" rel="stylesheet">
<style>
  :root {
    --backdrop: #f7e4e9;
    --card-white: #fbfbfb;
    --card-grey: #e6e6e6;
    --blush: #d9a2b2;
    --rose: #c98a9d;
    --ink-grey: #7d7d7d;
    --band-text: #ffffff;
  }
  * { margin: 0; padding: 0; box-sizing: border-box; }
  html, body { width: 1200px; height: 1000px; overflow: hidden; }
  body {
    background: var(--backdrop);
    display: flex;
    align-items: center;
    justify-content: center;
  }
  .business-card {
    position: relative;
    width: 840px;
    height: 480px;
    background: var(--card-white);
    box-shadow: 0 10px 30px rgba(150, 90, 110, 0.18);
    overflow: hidden;
  }
  .card-pattern {
    position: absolute;
    inset: 0 0 52px 0;
    background: radial-gradient(ellipse at center, var(--card-white) 0%, #f6eef1 55%, #efdde3 100%);
  }
  .brand-lockup {
    position: absolute;
    left: 0; right: 0;
    top: 150px;
    display: flex;
    align-items: center;
    justify-content: center;
    gap: 26px;
  }
  .brand-dot {
    width: 96px;
    height: 96px;
    border-radius: 50%;
    background: var(--blush);
    flex: none;
  }
  .brand-words { text-align: center; }
  .brand-name {
    font-family: 'Cinzel', serif;
    font-weight: 400;
    font-size: 54px;
    letter-spacing: 2px;
    color: var(--ink-grey);
    line-height: 1;
    padding-bottom: 10px;
    border-bottom: 2px solid var(--blush);
  }
  .brand-sub {
    font-family: 'Cinzel', serif;
    font-weight: 400;
    font-size: 26px;
    letter-spacing: 22px;
    margin-right: -22px;
    color: var(--ink-grey);
    padding-top: 10px;
  }
  .contact-band {
    position: absolute;
    left: 0; right: 0; bottom: 0;
    height: 52px;
    background: var(--rose);
    display: flex;
    align-items: center;
    justify-content: space-between;
    padding: 0 34px;
    font-family: 'Roboto', sans-serif;
    font-size: 17px;
    color: var(--band-text);
  }
  .contact-item { display: flex; align-items: center; gap: 10px; }
  .contact-mark {
    width: 16px; height: 16px;
    border-radius: 50%;
    background: var(--band-text);
  }
  .contact-icon { width: 20px; height: 14px; }
</style>
</head>
<body>
  <div class="business-card">
    <div class="card-pattern" role="img" aria-label="Fine pink swirl and flourish pattern covering the card face"></div>

    <div class="brand-lockup">
      <div class="brand-dot"></div>
      <div class="brand-words">
        <div class="brand-name">Aunt Rolina's</div>
        <div class="brand-sub">Bakery</div>
      </div>
    </div>

    <div class="contact-band">
      <div class="contact-item">
        <span class="contact-mark"></span>
        <span>aunt_rolina_bakery</span>
      </div>
      <div class="contact-item">
        <svg class="contact-icon" viewBox="0 0 20 14" aria-hidden="true">
          <rect x="1" y="1" width="18" height="12" rx="1.5" fill="none" stroke="#ffffff" stroke-width="1.6"/>
          <path d="M1.5 1.8 L10 8 L18.5 1.8" fill="none" stroke="#ffffff" stroke-width="1.6"/>
        </svg>
        <span>auntrolinasbakery@maplecrumbmail.com</span>
      </div>
    </div>
  </div>
</body>
</html>
```